IT Freelancer (Consulting, trainer and project manager) needed letterhead

As a freelancer for IT Trainingswhip, consulting and project management I need a letterhead design. What is desired is a design that fits the existing logo (see Annex). It is functional, reliable, and equal time wirkenn Agil and modern. The whole is in color, as well as printed out to make a good impression on a black and white printer. The whole is to the existing Cooperate design (business card, homepage, logo) fit. Therefore, the choice of colors.

Target Market(s)

Customers such as medium-sized enterprises, training institutions

Industry/Entity Type

Consulting

Colors
0455a3
3277b5
85abd2
cfdfed
34a6d7
32a6d6
249fd4
0792cd
85cae6

Requirements
Must have
• Must include logo (see Annex) address (Ahornweg 14, 84317 Lindenau, Germany). Must seriously and act simultaneously Agil. Design should (even) be adaptable (signature, address, etc.) design must look good on a black / white laser

```html
<!DOCTYPE html>
<html lang="de">
<head>
<meta charset="utf-8">
<title>Lorenz Hafner – Briefbogen</title>
<link href="https://fonts.googleapis.com/css2?family=Source+Sans+3:wght@400;700&family=Great+Vibes&display=swap" rel="stylesheet">
<style>
  :root {
    --blue-deep: #0455a3;
    --blue-mid: #3277b5;
    --blue-pale: #cfdfed;
    --blue-sky: #29abe2;
    --blue-bright: #249fd4;
    --blue-base: #0070bb;
    --grey-soft: #eeeeee;
    --ink-signature: #1c3d70;
    --mark-faint: #e6eef7;
    --white: #ffffff;
  }
  html, body {
    margin: 0;
    padding: 0;
    overflow: hidden;
    background: var(--white);
  }
  .letterhead {
    position: relative;
    width: 849px;
    height: 1200px;
    overflow: hidden;
    background: var(--white);
    font-family: "Source Sans 3", sans-serif;
  }
  .letterhead__waves {
    position: absolute;
    inset: 0;
    width: 849px;
    height: 1200px;
  }
  .brand-badge {
    position: absolute;
    left: 56px;
    top: 50px;
    width: 188px;
    height: 188px;
    border-radius: 50%;
    background: var(--white);
    display: flex;
    flex-direction: column;
    align-items: center;
  }
  .brand-badge__dot {
    width: 92px;
    height: 92px;
    border-radius: 50%;
    background: var(--blue-bright);
    margin-top: 28px;
  }
  .brand-badge__name {
    color: var(--blue-deep);
    font-weight: 700;
    font-size: 21px;
    line-height: 1.0;
    letter-spacing: 1.5px;
    text-align: center;
    margin: 8px 0 0;
  }
  .watermark {
    position: absolute;
    left: 0;
    width: 849px;
    top: 388px;
    text-align: center;
  }
  .watermark__disc {
    width: 280px;
    height: 280px;
    border-radius: 50%;
    background: var(--mark-faint);
    margin: 0 auto;
  }
  .watermark__name {
    color: var(--mark-faint);
    font-weight: 700;
    font-size: 74px;
    line-height: 0.98;
    letter-spacing: 6px;
    margin: 22px 0 0;
  }
  .signature {
    position: absolute;
    left: 72px;
    top: 942px;
    width: 170px;
  }
  .signature__text {
    font-family: "Great Vibes", cursive;
    color: var(--ink-signature);
    font-size: 48px;
    line-height: 1;
    margin: 0;
  }
  .signature__line {
    height: 1px;
    background: var(--ink-signature);
    opacity: 0.6;
    margin-top: 2px;
  }
  .address {
    position: absolute;
    right: 27px;
    top: 1162px;
    display: flex;
    align-items: center;
    gap: 5px;
    color: var(--white);
    font-size: 18.5px;
    letter-spacing: -0.3px;
    margin: 0;
    white-space: nowrap;
  }
  .address__pin {
    width: 15px;
    height: 22px;
  }
</style>
</head>
<body>
<div class="letterhead">
  <svg class="letterhead__waves" viewBox="0 0 1061 1500" preserveAspectRatio="none" aria-hidden="true">
    <rect x="0" y="0" width="1061" height="520" fill="var(--blue-deep)"/>
    <path d="M0 230 C250 110 700 45 1061 28 L1061 520 L0 520 Z" fill="var(--blue-mid)"/>
    <path d="M0 305 C250 170 700 80 1061 62 L1061 520 L0 520 Z" fill="var(--blue-pale)"/>
    <path d="M0 425 C80 250 500 110 1061 68 L1061 1500 L0 1500 Z" fill="var(--white)"/>
    <path d="M0 1445 C500 1410 900 1285 1061 1110 L1061 1500 L0 1500 Z" fill="var(--grey-soft)"/>
    <path d="M0 1448 C450 1440 850 1345 1061 1215 L1061 1500 L0 1500 Z" fill="var(--blue-sky)"/>
    <path d="M0 1481 C450 1472 850 1395 1061 1255 L1061 1500 L0 1500 Z" fill="var(--blue-base)"/>
  </svg>

  <header class="brand-badge">
    <div class="brand-badge__dot"></div>
    <p class="brand-badge__name">LORENZ<br>HAFNER</p>
  </header>

  <div class="watermark" aria-hidden="true">
    <div class="watermark__disc"></div>
    <p class="watermark__name">LORENZ<br>HAFNER</p>
  </div>

  <div class="signature">
    <p class="signature__text">Signature</p>
    <div class="signature__line"></div>
  </div>

  <footer>
    <p class="address">
      <svg class="address__pin" viewBox="0 0 15 22" aria-hidden="true">
        <path d="M7.5 0 C3.4 0 0 3.3 0 7.4 C0 12.8 7.5 22 7.5 22 C7.5 22 15 12.8 15 7.4 C15 3.3 11.6 0 7.5 0 Z M7.5 10.4 A3 3 0 1 1 7.5 4.4 A3 3 0 1 1 7.5 10.4 Z" fill="var(--white)"/>
      </svg>
      Ahornweg 14, 84317 Lindenau, Deutschland
    </p>
  </footer>
</div>
</body>
</html>
```